Summit Grading a Masonry LLC business card

My current business card is very plain. it has my logo and contact information. I woud like something that stands out from the rest. please take a look at my website to see about my company.

Compayt Name - Summit Grading And Masonry
Owner - Martin Galloway
Business Address
Business Website - www.summitgradingandmasonry.example
Email - Summitgradingandmasonry@mailbox.example
Phone - 555-214-3867
Fax - 555-630-2719

Target Market(s)

Everyone age tang is 18 - 85

Industry/Entity Type

Business

Contact Information for Business Card

Nice and professional all in one.

Font styles to use
Serif
Other font styles liked:
• Up to you

Requirements
Must have
• All contact info. The design is up to you.
Nice to have
• All the contact info the design is up to you
Should not have
• I don't have any

```html
<!DOCTYPE html>
<html lang="en">
<head>
<meta charset="utf-8">
<title>Summit Grading &amp; Masonry LLC — Business Card</title>
<link rel="stylesheet" href="https://fonts.googleapis.com/css2?family=Libre+Baskerville:wght@400;700&display=swap">
<style>
  :root {
    --backdrop: #1f1f1f;
    --card-white: #ffffff;
    --card-black: #262626;
    --swoosh-grey: #8c8c8c;
    --ink-dark: #3a3a3a;
    --ink-light: #f2f2f2;
    --ink-muted: #9a9a9a;
    --icon-grey: #7d8790;
    --badge-orange: #f08a24;
    --badge-steel: #cfd4d8;
  }
  * { margin: 0; padding: 0; box-sizing: border-box; }
  html, body {
    width: 1200px; height: 852px; overflow: hidden;
    background: var(--backdrop);
    font-family: "Libre Baskerville", Georgia, serif;
  }
  .sheet {
    width: 1200px; height: 852px;
    display: flex; align-items: center; justify-content: center; gap: 30px;
  }
  .card {
    position: relative; width: 560px; height: 320px;
    border-radius: 18px; overflow: hidden;
    background: var(--card-white);
    box-shadow: 0 10px 30px rgba(0,0,0,.5);
  }
  .card svg.card-shape { position: absolute; inset: 0; }
  .company-name {
    position: absolute;
    font-weight: 700; text-transform: uppercase;
    color: var(--ink-dark); line-height: 1.15; letter-spacing: .5px;
  }
  .card--front .company-name { left: 120px; top: 112px; font-size: 27px; }
  .card--back .company-name { left: 28px; top: 44px; font-size: 19px; }

  .owner { position: absolute; right: 30px; top: 112px; text-align: right; }
  .owner-name { color: var(--ink-light); font-size: 15px; font-weight: 700; }
  .owner-title { color: var(--ink-muted); font-size: 13px; margin-top: 2px; }

  .contact {
    position: absolute; left: 180px; top: 196px;
    color: var(--ink-light); font-size: 11px; line-height: 1.55;
  }
  .contact-row { display: flex; align-items: center; gap: 6px; }
  .contact-icon {
    width: 13px; height: 13px; border-radius: 2px;
    background: var(--icon-grey);
    display: inline-flex; align-items: center; justify-content: center;
  }
  .address { margin-bottom: 4px; }

  .badges {
    position: absolute; right: 30px; top: 176px;
    display: flex; gap: 14px; align-items: center;
  }
  .website {
    position: absolute; right: 30px; bottom: 22px;
    color: var(--ink-light); font-size: 12px; font-weight: 700; letter-spacing: 2.5px;
  }
</style>
</head>
<body>
<main class="sheet">

  <section class="card card--front" aria-label="Card front">
    <svg class="card-shape" width="560" height="320" viewBox="0 0 560 320" aria-hidden="true">
      <path fill="var(--swoosh-grey)"
        d="M560,8 C320,30 40,120 48,228 C54,292 150,316 250,320 L310,320
           C190,308 82,278 84,226 C90,134 330,52 560,30 Z"/>
    </svg>
    <h1 class="company-name">Summit Grading<br>&amp; Masonry LLC</h1>
  </section>

  <section class="card card--back" aria-label="Card back">
    <svg class="card-shape" width="560" height="320" viewBox="0 0 560 320" aria-hidden="true">
      <path fill="var(--swoosh-grey)" d="M20,320 C100,150 320,40 560,16 L560,52 C330,72 130,170 58,320 Z"/>
      <path fill="var(--card-black)" d="M58,320 C130,170 330,72 560,52 L560,320 Z"/>
    </svg>
    <h2 class="company-name">Summit Grading<br>&amp; Masonry LLC</h2>

    <div class="owner">
      <p class="owner-name">Martin Galloway</p>
      <p class="owner-title">Owner</p>
    </div>

    <div class="badges" aria-label="Service badges">
      <svg width="40" height="40" viewBox="0 0 40 40" aria-hidden="true">
        <circle cx="20" cy="20" r="18" fill="var(--badge-steel)" stroke="#fff" stroke-width="2"/>
        <rect x="6" y="17" width="28" height="7" fill="var(--badge-orange)"/>
      </svg>
      <svg width="36" height="40" viewBox="0 0 36 40" aria-hidden="true">
        <path d="M18,2 L34,10 L34,28 L18,38 L2,28 L2,10 Z" fill="var(--badge-steel)"/>
        <rect x="2" y="16" width="32" height="9" fill="var(--badge-orange)"/>
      </svg>
      <svg width="36" height="40" viewBox="0 0 36 40" aria-hidden="true">
        <path d="M4,4 L32,4 L32,30 L18,38 L4,30 Z" fill="var(--badge-orange)"/>
        <rect x="4" y="4" width="28" height="9" fill="var(--badge-steel)"/>
      </svg>
    </div>

    <div class="contact">
      <p class="address">2280 Harbor Lane Unit 400<br>Fairview, IL 60099</p>
      <p class="contact-row">
        <span class="contact-icon">
          <svg width="9" height="7" viewBox="0 0 9 7" aria-hidden="true"><rect x=".5" y=".5" width="8" height="6" fill="none" stroke="#fff"/><path d="M.5,.5 L4.5,4 L8.5,.5" fill="none" stroke="#fff"/></svg>
        </span>Summitgradingandmasonry@mailbox.example
      </p>
      <p class="contact-row">
        <span class="contact-icon">
          <svg width="9" height="9" viewBox="0 0 9 9" aria-hidden="true"><path d="M1,1 L3,1 L4,3 L3,4 C4,5.5 4.5,6 5,6 L6,5 L8,6 L8,8 C4,8 1,5 1,1 Z" fill="#fff"/></svg>
        </span>555-214-3867
      </p>
      <p class="contact-row">
        <span class="contact-icon">
          <svg width="9" height="9" viewBox="0 0 9 9" aria-hidden="true"><rect x="2" y="1" width="5" height="3" fill="#fff"/><rect x="1" y="4" width="7" height="4" fill="#fff"/></svg>
        </span>555-630-2719
      </p>
    </div>

    <p class="website">www.summitgradingandmasonry.example</p>
  </section>

</main>
</body>
</html>
```